Brand: Comet Gherkin; watermelon pickle pouch packaging design, flavor: WATERMELON SANDIA

can you design a pouch for a watermelon-flavored pickle, you should be using bold colors and designs, also maybe background could be a slice of watermelon, we want bright colors, and an eye catching design, also maybe have a pickle character on it, i have attached a picture of a pickle pouch for example.. .........................................................................

Target Market(s)

all people, mostly younger people

Industry/Entity Type

pickles, candy

Colors
00AB8E
00BBA5
67D7C9
C6EFE9
E9F9F6
FFF300
FFF600
FEFA6F
FFFEC7
FFFEE8
EB3D1F
EC4F4E
F09395
F8D3D4
FCEDEE
E54698
E96AAD
F1A4CE
F9D9EA
FCEFF6

Requirements
Must have
• bright colors, like bright green and hot pink, and maybe bright yellow, can you please use the same red as the watermelon in the photo attached? the design needs to look juicy and appetizing
Nice to have
• watermelon background like watermelon sliced with the seeds, font of words should be in black bubble letters, and a window
Should not have
• n/a

```html
<!DOCTYPE html>
<html lang="en">
<head>
<meta charset="utf-8">
<title>Comet Gherkin — Watermelon Pickle Pouch</title>
<link rel="stylesheet" href="https://fonts.googleapis.com/css2?family=Lilita+One&family=Montserrat:wght@500&display=swap">
<style>
  :root {
    --backdrop: #e6e6e6;
    --melon-red: #c41a35;
    --melon-red-deep: #b3172f;
    --rind-green: #0c5631;
    --rind-pale: #c9dfc6;
    --title-yellow: #d9d30c;
    --subtitle: #e4ece2;
    --window-grey: #b3b4b6;
    --seal-gold: #e9d81a;
  }
  html, body {
    margin: 0;
    padding: 0;
    width: 1200px;
    height: 1200px;
    overflow: hidden;
    background: var(--backdrop);
  }
  .canvas {
    width: 1200px;
    height: 1200px;
    display: block;
  }
  .pouch-body { fill: var(--melon-red); }
  .zip-seal { fill: var(--melon-red-deep); }
  .flesh-pattern { fill: var(--melon-red); }
  .label-band { fill: var(--rind-green); stroke: var(--rind-pale); stroke-width: 7; }
  .product-window { fill: var(--window-grey); stroke: var(--rind-pale); stroke-width: 6; stroke-linejoin: round; }
  .organic-seal { fill: var(--seal-gold); }
  .brand-title {
    font-family: "Lilita One", sans-serif;
    fill: var(--title-yellow);
    font-size: 112px;
  }
  .flavor-line {
    font-family: "Montserrat", sans-serif;
    font-weight: 500;
    fill: var(--subtitle);
    font-size: 19px;
    letter-spacing: 0.5px;
  }
</style>
</head>
<body>
<svg class="canvas" viewBox="0 0 1200 1200" xmlns="http://www.w3.org/2000/svg">
  <g class="pouch">
    <rect class="pouch-body" x="326" y="165" width="548" height="865" rx="24"/>
    <rect class="zip-seal" x="352" y="270" width="496" height="8" rx="4"/>

    <g role="img" aria-label="Watermelon flesh with scattered seeds">
      <rect class="flesh-pattern" x="326" y="285" width="548" height="170"/>
      <rect class="flesh-pattern" x="340" y="780" width="520" height="235" rx="20"/>
    </g>

    <path class="label-band"
      d="M334 428
         C 390 410, 440 372, 497 370
         C 550 368, 580 412, 621 413
         C 670 414, 710 355, 764 357
         C 810 359, 840 420, 862 452
         L 844 810
         C 810 822, 780 850, 764 862
         C 720 900, 660 935, 596 936
         C 560 936, 520 918, 482 912
         C 430 880, 390 820, 357 770
         Z"/>

    <path class="product-window"
      d="M590 740 Q597 728 604 740 L666 924 Q630 937 596 937 Q545 937 503 913 Z"/>

    <circle class="organic-seal" cx="709" cy="885" r="54"/>

    <text class="brand-title" x="600" y="553" text-anchor="middle" textLength="360" lengthAdjust="spacingAndGlyphs">COMET</text>
    <text class="brand-title" x="600" y="670" text-anchor="middle" textLength="372" lengthAdjust="spacingAndGlyphs">GHERKIN</text>
    <text class="flavor-line" x="597" y="705" text-anchor="middle" textLength="366" lengthAdjust="spacingAndGlyphs">WATERMELON-FLAVORED PICKLE</text>
  </g>
</svg>
</body>
</html>
```